Anzeigengestaltung für KFZ-Rundumservice
Zielgruppe
KFZ - Rundumservice
- Kundendienst aller Marken nach Herstellervorgabe
- Unfallinstandsetzung
- Karosseriearbeiten
- Lackierarbeiten
- Kundenersatzfahrzeuge
Ab sofort im Haus tägliche Hauptuntersuchung nach

```html
<!DOCTYPE html>
<html lang="de">
<head>
<meta charset="utf-8">
<title>Kessler – KFZ-Rundumservice Anzeige</title>
<link href="https://fonts.googleapis.com/css2?family=Outfit:wght@400;500;600;700&display=swap" rel="stylesheet">
<style>
  :root{
    --sheet:#e6e6e6;
    --yellow:#fbdb1f;
    --dark:#4a4a4c;
    --white:#ffffff;
    --photo-light:#eef2f5;
    --photo-pale:#dde3e8;
    --photo-mid:#8f969e;
    --photo-warm:#6b625c;
    --photo-dark:#353334;
  }
  *{box-sizing:border-box;margin:0;padding:0}
  html,body{width:720px;height:1200px;overflow:hidden;background:var(--sheet);font-family:"Outfit",Arial,sans-serif}
  .sheet{position:relative;width:720px;height:1200px}
  .ad{position:absolute;left:104px;width:513px;height:470px;background:var(--white);overflow:hidden;color:var(--dark)}
  .ad--first{top:93px}
  .ad--second{top:634px}
  .ad__photo{position:absolute;left:0;top:116px;width:513px;height:330px;
    background:linear-gradient(90deg, var(--photo-light) 0%, var(--photo-pale) 32%, var(--photo-mid) 55%, var(--photo-warm) 78%, var(--photo-dark) 100%);}
  .ad__band{position:absolute;left:180px;top:0;width:333px;height:118px;background:var(--yellow);border-bottom:3px solid var(--dark)}
  .ad__car{position:absolute;left:0;top:0;width:181px;height:163px;
    background:linear-gradient(160deg, var(--white) 0%, var(--white) 22%, var(--yellow) 48%, var(--yellow) 100%);}
  .ad__tab{position:absolute;left:233px;top:0;width:160px;height:32px;background:var(--dark);
    clip-path:polygon(0 0,100% 0,94% 100%,6% 100%);border-radius:0 0 10px 10px;
    color:var(--yellow);font-weight:600;font-size:20.5px;letter-spacing:-.3px;text-align:center;line-height:32px}
  .ad__headline{position:absolute;left:130px;top:47px;width:360px;text-align:center;font-weight:500;font-size:20px;line-height:22px;letter-spacing:-.3px;color:var(--dark)}
  .phone{position:absolute;left:185px;top:99px;height:37px}
  .phone__pill{position:absolute;left:31px;top:4px;width:222px;height:29px;background:var(--dark);border-radius:0 14px 14px 0;
    color:var(--yellow);font-weight:600;font-size:20px;line-height:29px;padding-left:22px;white-space:nowrap}
  .phone__icon{position:absolute;left:0;top:0;width:37px;height:37px}
  .service-bar{position:absolute;left:0;top:163px;width:206px;height:27px;background:var(--dark);border-radius:0 14px 14px 0;
    color:var(--yellow);font-weight:600;font-size:18px;line-height:27px;padding-left:21px;letter-spacing:-.3px;white-space:nowrap}
  .services{position:absolute;left:22px;top:209px;list-style:none}
  .services li{position:relative;padding-left:17px;font-weight:500;font-size:14px;line-height:16px;margin-bottom:10.5px;letter-spacing:-.1px}
  .services li:first-child{margin-bottom:10px}
  .services svg{position:absolute;left:0;top:2.5px;width:11px;height:11px}
  .brand{position:absolute;left:72px;top:378px}
  .brand__name{display:block;color:var(--yellow);font-weight:700;font-size:34px;line-height:34px;letter-spacing:1px}
  .brand__line{display:block;margin-left:-14px;margin-top:2px;font-weight:400;font-size:10.5px;color:var(--dark)}
  .footer{position:absolute;left:0;bottom:0;width:513px;display:flex;font-weight:600;line-height:12px;text-align:center}
  .footer__web{width:256px;background:var(--dark);color:var(--white);font-size:10px;letter-spacing:.5px;display:flex;flex-direction:column;justify-content:center}
  .footer__address{flex:1;background:var(--yellow);color:var(--dark);font-size:10.5px;display:flex;flex-direction:column;justify-content:center}
  .ad--first .footer{height:25px}
  .ad--second .footer{height:34px}
</style>
</head>
<body>
<div class="sheet">

  <section class="ad ad--first">
    <div class="ad__photo" role="img" aria-label="Foto: Mechaniker-Hände mit Ratsche am Motorraum eines Autos"></div>
    <div class="ad__band"></div>
    <div class="ad__car" role="img" aria-label="Illustration: gelbe Autosilhouette"></div>
    <div class="ad__tab">AB SOFORT:</div>
    <h2 class="ad__headline">Tägliche Hauptuntersuchung im Haus<br>nach §29 StVZO</h2>
    <div class="phone">
      <div class="phone__pill">Telefon 07321-4096</div>
      <svg class="phone__icon" viewBox="0 0 37 37" aria-hidden="true">
        <circle cx="18.5" cy="18.5" r="17" fill="var(--yellow)" stroke="var(--dark)" stroke-width="3"/>
        <path d="M12,10 l4,-1 l2,5 l-2.5,2 c1,2.5 3,4.5 5.5,5.5 l2,-2.5 l5,2 l-1,4 c-9,1 -16,-6 -15,-15 z" fill="var(--dark)"/>
        <path d="M20,11 a7,7 0 0 1 6,6 M20,7.5 a10.5,10.5 0 0 1 9.5,9.5" fill="none" stroke="var(--dark)" stroke-width="1.5"/>
      </svg>
    </div>
    <div class="service-bar">KFZ - Rundumservice</div>
    <ul class="services">
      <li><svg viewBox="0 0 12 12"><circle cx="6" cy="6" r="5" fill="none" stroke="var(--dark)" stroke-width="1.3"/><path d="M3.3,6 l2,2 l4.5,-5" fill="none" stroke="var(--dark)" stroke-width="1.5"/></svg>Kundendienst aller Marken<br>nach Herstellervorgabe</li>
      <li><svg viewBox="0 0 12 12"><circle cx="6" cy="6" r="5" fill="none" stroke="var(--dark)" stroke-width="1.3"/><path d="M3.3,6 l2,2 l4.5,-5" fill="none" stroke="var(--dark)" stroke-width="1.5"/></svg>Unfallinstandsetzung</li>
      <li><svg viewBox="0 0 12 12"><circle cx="6" cy="6" r="5" fill="none" stroke="var(--dark)" stroke-width="1.3"/><path d="M3.3,6 l2,2 l4.5,-5" fill="none" stroke="var(--dark)" stroke-width="1.5"/></svg>Karosseriearbeiten</li>
      <li><svg viewBox="0 0 12 12"><circle cx="6" cy="6" r="5" fill="none" stroke="var(--dark)" stroke-width="1.3"/><path d="M3.3,6 l2,2 l4.5,-5" fill="none" stroke="var(--dark)" stroke-width="1.5"/></svg>Lackierarbeiten</li>
      <li><svg viewBox="0 0 12 12"><circle cx="6" cy="6" r="5" fill="none" stroke="var(--dark)" stroke-width="1.3"/><path d="M3.3,6 l2,2 l4.5,-5" fill="none" stroke="var(--dark)" stroke-width="1.5"/></svg>Kundenersatzfahrzeuge</li>
    </ul>
    <div class="brand">
      <span class="brand__name">KESSLER</span>
      <span class="brand__line">Autolackierung &amp; Karosserietechnik</span>
    </div>
    <footer class="footer">
      <div class="footer__web">www.autolackierung-kessler.de</div>
      <div class="footer__address">Werkstraße 14 | 89520 Talheim</div>
    </footer>
  </section>

  <section class="ad ad--second">
    <div class="ad__photo" role="img" aria-label="Foto: Mechaniker-Hände mit Ratsche am Motorraum eines Autos"></div>
    <div class="ad__band"></div>
    <div class="ad__car" role="img" aria-label="Illustration: gelbe Autosilhouette"></div>
    <div class="ad__tab">AB SOFORT:</div>
    <h2 class="ad__headline">Tägliche Hauptuntersuchung im Haus<br>nach §29 StVZO</h2>
    <div class="phone">
      <div class="phone__pill">Telefon 07321-4096</div>
      <svg class="phone__icon" viewBox="0 0 37 37" aria-hidden="true">
        <circle cx="18.5" cy="18.5" r="17" fill="var(--yellow)" stroke="var(--dark)" stroke-width="3"/>
        <path d="M12,10 l4,-1 l2,5 l-2.5,2 c1,2.5 3,4.5 5.5,5.5 l2,-2.5 l5,2 l-1,4 c-9,1 -16,-6 -15,-15 z" fill="var(--dark)"/>
        <path d="M20,11 a7,7 0 0 1 6,6 M20,7.5 a10.5,10.5 0 0 1 9.5,9.5" fill="none" stroke="var(--dark)" stroke-width="1.5"/>
      </svg>
    </div>
    <div class="service-bar">KFZ - Rundumservice</div>
    <ul class="services">
      <li><svg viewBox="0 0 12 12"><circle cx="6" cy="6" r="5" fill="none" stroke="var(--dark)" stroke-width="1.3"/><path d="M3.3,6 l2,2 l4.5,-5" fill="none" stroke="var(--dark)" stroke-width="1.5"/></svg>Kundendienst aller Marken<br>nach Herstellervorgabe</li>
      <li><svg viewBox="0 0 12 12"><circle cx="6" cy="6" r="5" fill="none" stroke="var(--dark)" stroke-width="1.3"/><path d="M3.3,6 l2,2 l4.5,-5" fill="none" stroke="var(--dark)" stroke-width="1.5"/></svg>Unfallinstandsetzung</li>
      <li><svg viewBox="0 0 12 12"><circle cx="6" cy="6" r="5" fill="none" stroke="var(--dark)" stroke-width="1.3"/><path d="M3.3,6 l2,2 l4.5,-5" fill="none" stroke="var(--dark)" stroke-width="1.5"/></svg>Karosseriearbeiten</li>
      <li><svg viewBox="0 0 12 12"><circle cx="6" cy="6" r="5" fill="none" stroke="var(--dark)" stroke-width="1.3"/><path d="M3.3,6 l2,2 l4.5,-5" fill="none" stroke="var(--dark)" stroke-width="1.5"/></svg>Lackierarbeiten</li>
      <li><svg viewBox="0 0 12 12"><circle cx="6" cy="6" r="5" fill="none" stroke="var(--dark)" stroke-width="1.3"/><path d="M3.3,6 l2,2 l4.5,-5" fill="none" stroke="var(--dark)" stroke-width="1.5"/></svg>Kundenersatzfahrzeuge</li>
    </ul>
    <div class="brand">
      <span class="brand__name">KESSLER</span>
      <span class="brand__line">Autolackierung &amp; Karosserietechnik</span>
    </div>
    <footer class="footer">
      <div class="footer__web">www.autolackierung-kessler.de<br>Telefon: 07321 - 4096</div>
      <div class="footer__address">Autolackierung &amp; Karosserietechnik Kessler<br>Werkstraße 14 | 89520 Talheim</div>
    </footer>
  </section>

</div>
</body>
</html>
```